Create a Magazine Ad for an asbestos law firm

we need an 8 X 13 ad to be on the back of a magazine cover. We have the text Attached and want a similar look and feel to our website : www.claimsharbor-help.com. The ad should be targeted to white males 55 years or older who are conservative and worked in industry or industrial plants. The main offer is a free case review and trying to get them to call the telephone number.

Target Market(s)

White collar men who worked in industrial plants. Age 55 years or older.

Industry/Entity Type

Legal

Requirements
Must have
• Pictures of white middle class conservative man or man and woman
Nice to have
• look at www.claimsharbor-help.com to an. idea of what we are looking for

```html
<!DOCTYPE html>
<html lang="en">
<head>
<meta charset="utf-8">
<title>Mesothelioma Compensation – Magazine Ad</title>
<link href="https://fonts.googleapis.com/css2?family=Oswald:wght@500;600;700&family=Arimo:ital,wght@0,400;0,700;1,700&display=swap" rel="stylesheet">
<style>
  :root{
    --stage:#7d6c65;
    --paper:#ffffff;
    --brown:#5b4a42;
    --brown-dark:#352a25;
    --tan:#b5a78f;
    --tan-light:#d9cfbf;
    --ink:#4a3c35;
    --skin:#d2b8a2;
    --skin-deep:#b89a84;
  }
  *{box-sizing:border-box;margin:0;padding:0}
  html,body{width:1200px;height:821px;overflow:hidden;background:var(--stage)}
  body{font-family:"Arimo",Arial,sans-serif;position:relative}
  .ad{position:absolute;left:354px;top:10px;width:492px;height:800px;background:var(--paper);overflow:hidden}

  .portrait{position:absolute;left:150px;top:0;width:342px;height:427px;
    background:
      radial-gradient(ellipse 55% 45% at 68% 48%,rgba(214,186,164,.95) 0%,rgba(214,186,164,.55) 55%,rgba(214,186,164,0) 100%),
      radial-gradient(ellipse 40% 30% at 70% 80%,rgba(236,232,226,.9) 0%,rgba(236,232,226,0) 100%),
      linear-gradient(180deg,#e6d8ca 0%,var(--skin) 45%,var(--skin-deep) 100%);}
  .portrait-fade{position:absolute;left:150px;top:0;width:200px;height:427px;background:linear-gradient(90deg,#fff 0%,rgba(255,255,255,.75) 45%,rgba(255,255,255,0) 100%)}

  .question-mark{position:absolute;left:344px;top:46px;font-family:"Oswald",sans-serif;font-weight:700;font-size:150px;line-height:1;color:rgba(150,110,80,.25)}
  .headline{position:absolute;left:40px;top:58px;font-family:"Oswald",sans-serif;font-weight:700;font-size:49px;line-height:54px;color:var(--ink);letter-spacing:-.3px}
  .subhead-brush{position:absolute;left:185px;top:184px;width:225px;height:16px}
  .subhead{position:absolute;left:40px;top:168px;font-family:"Oswald",sans-serif;font-weight:600;font-size:25px;line-height:30px;color:var(--ink)}
  .intro{position:absolute;left:40px;top:210px;width:330px;font-weight:700;font-size:12.2px;line-height:15.4px;color:var(--ink)}
  .sources{position:absolute;left:40px;top:277px;list-style:none}
  .sources li{width:190px;height:14px;margin-bottom:3px;padding-left:5px;font-size:11px;line-height:14px;color:var(--ink);background:linear-gradient(90deg,var(--tan-light),rgba(217,207,191,0))}
  .sources li::before{content:"• "}

  .qualify-band{position:absolute;left:0;top:338px;width:492px;height:90px}
  .qualify{position:absolute;left:40px;top:349px}
  .qualify h3{font-style:italic;font-weight:700;font-size:11.5px;line-height:14.5px;color:var(--ink);margin-bottom:4px}
  .qualify li{list-style:none;font-size:8.2px;line-height:12.6px;color:var(--ink)}
  .qualify li::before{content:"•  "}

  .details{position:absolute;left:0;top:427px;width:492px;height:373px;background:var(--brown)}
  .details-base{position:absolute;left:0;bottom:0;width:492px;height:15px;background:var(--brown-dark)}
  .col{position:absolute;top:28px;color:#fff;width:200px}
  .col h2{font-weight:700;font-size:11.3px;line-height:14px;margin-bottom:10px}
  .col p{font-size:7.8px;line-height:10.2px;color:#f0e9e2;white-space:nowrap}
  .col-trust{left:40px}
  .col-amounts{left:263px;top:27px}
  .col-amounts h2{margin-bottom:9px}

  .settlements{position:absolute;left:40px;top:152px;list-style:none}
  .settlements li{display:flex;gap:6px;margin-bottom:6.6px}
  .amount{width:95px;height:24px;background:var(--brown-dark);font-family:"Oswald",sans-serif;font-weight:500;font-size:18px;line-height:24px;text-align:right;padding-right:5px;color:#fff;white-space:nowrap}
  .amount-words{font-size:16.5px;letter-spacing:-.2px}
  .source{width:100px;height:24px;background:var(--brown-dark);font-size:7.6px;line-height:9.4px;padding:3px 7px;color:#f0e9e2;white-space:nowrap}

  .cta{position:absolute;left:260px;top:152px;width:192px;height:177px;background:var(--brown-dark);padding:4px}
  .cta-frame{width:100%;height:100%;border:1px solid #e8e0d8;display:flex;flex-direction:column;color:#fff;text-align:center}
  .cta-offer{flex:0 0 84px;padding:15px 4px 0;font-size:8.6px;line-height:11.2px;border-bottom:1px solid #e8e0d8;white-space:nowrap}
  .cta-phone{flex:0 0 26px;font-family:"Oswald",sans-serif;font-weight:500;font-size:11.5px;line-height:25px;border-bottom:1px solid #e8e0d8}
  .cta-firm{flex:1;padding-top:12px;font-weight:700;font-size:9.2px;line-height:14px}
</style>
</head>
<body>
  <article class="ad">
    <div class="portrait" role="img" aria-label="Close-up portrait photo of an older bearded man, fading into white on the left"></div>
    <div class="portrait-fade" aria-hidden="true"></div>
    <div class="question-mark" aria-hidden="true">?</div>

    <h1 class="headline">Diagnosed with<br>Mesothelioma</h1>
    <svg class="subhead-brush" viewBox="0 0 225 16" aria-hidden="true"><path d="M2 10 C50 6 130 3 223 3 L221 8 C140 10 70 13 4 15 Z" fill="#ffffff"/></svg>
    <p class="subhead">You Could Be Owed Compensation</p>

    <p class="intro">It's very likely you developed this disease through asbestos exposure. Mesothelioma patients are getting multi-million dollar settlements, decades later, from:</p>
    <ul class="sources">
      <li>Exposure to asbestos products,</li>
      <li>Ex-employers, or</li>
      <li>Talcum baby powder companies.</li>
    </ul>

    <svg class="qualify-band" viewBox="0 0 492 90" aria-hidden="true">
      <defs><linearGradient id="tanFade" x1="0" x2="1" y1="0" y2="0"><stop offset="0" stop-color="#b5a78f"/><stop offset=".7" stop-color="#c6b9a4"/><stop offset="1" stop-color="#d3c7b5"/></linearGradient></defs>
      <path d="M0 14 Q0 0 14 0 L290 0 Q302 0 307 10 L346 90 L0 90 Z" fill="url(#tanFade)"/>
    </svg>
    <section class="qualify">
      <h3>We can help you find out if<br>you qualify for a case in minutes</h3>
      <ul>
        <li>We'll analyze your situation at no cost</li>
        <li>Determine how much compensation you could be entitled too</li>
        <li>Show you the next steps to get what you're owed</li>
      </ul>
    </section>

    <section class="details">
      <div class="col col-trust">
        <h2>$30 Billion is Available in Trust<br>for Mesothelioma Patients</h2>
        <p>Tradesmen in many industries were negligently<br>exposed to asbestos materials well into the 1990s.<br>Whether you developed Mesothelioma yourself<br>due to asbestos exposure or you're the surviving<br>family of a lost loved one you could be entitled to<br>significant compensation.</p>
      </div>
      <div class="col col-amounts">
        <h2>How much Money Can People<br>Receive from a Mesothelioma<br>Case?</h2>
        <p>Depending on where you were exposed and a<br>few other factors, you can get a settlement from 6<br>to 7 figures. Here are a few examples of Mesothe-<br>lioma Settlements received by our clients. These<br>figures are the total compensation after all<br>attorney fees and expenses are deducted.</p>
      </div>

      <ul class="settlements">
        <li><span class="amount">$6,142,500</span><span class="source">Exposed through<br>heavy duty vehicles</span></li>
        <li><span class="amount">$6,033,510</span><span class="source">Exposed through<br>general contracting</span></li>
        <li><span class="amount">$5,939,010</span><span class="source">Exposed through<br>boat repair</span></li>
        <li><span class="amount">$3,921,750</span><span class="source">Exposed through<br>navy service</span></li>
        <li><span class="amount">$3,600,450</span><span class="source">Exposed through<br>navy service</span></li>
        <li><span class="amount amount-words">$2.5 MILLION</span><span class="source">Exposed from Brightwell<br>Talcum Baby Powder</span></li>
      </ul>

      <aside class="cta">
        <div class="cta-frame">
          <p class="cta-offer"><strong>Find out if you're Eligible, for<br>FREE, in Minutes.</strong> We'll evaluate<br>your situation and tell you what your<br>case could be worth. Get your Free<br>evaluation now!</p>
          <p class="cta-phone">CALL 1-XXX XXXX (GOOD NUMBER)</p>
          <p class="cta-firm">Harrow &amp; Pell, LLP,<br>Martin Harrow, Houston, TX</p>
        </div>
      </aside>

      <div class="details-base"></div>
    </section>
  </article>
</body>
</html>
```